Contemporary new French wine brand needs logo and series of label design

to design a new contemporary logo and series of labels for a new French wine brand. We hope to attract not just current French wine drinkers but new ones who may appreciate a less traditional and more modern style.
Updates

Reason: we are wanting to extend the project for a few days more to receive more submissions since we had fewer designs submitted than we were expecting, maybe because of the holidays.

Target Market(s)

people who follow the arts community (eg. music, theatre, visual/video arts, dance) --- all mature ages.

Industry/Entity Type

French Wine

Requirements
Must have
• a clear, memorable treatment for the name CLAVINE with accompanying logo.
Nice to have
• embossing, matte/gloss refinement, tasteful foil stamping, coated stock for the whites to help the integrity of the paper in and out of ice buckets. A combo of say, three types of fonts; a semi custom font for the brand name Clavine and maybe a script and one other.
Should not have
• not traditional French

```html
<!DOCTYPE html>
<html lang="en">
<head>
<meta charset="UTF-8">
<title>Clavine — Burgundy Wine Label</title>
<link href="https://fonts.googleapis.com/css2?family=Josefin+Sans:wght@300;400&family=Pinyon+Script&family=Cormorant+Garamond:wght@500&display=swap" rel="stylesheet">
<style>
  :root {
    --backdrop: #e6e6e4;
    --label-stock: #f6f6f4;
    --gold: #eebf4f;
    --stripe-grey: #b3b3b3;
    --slate: #6f6f6f;
    --ink: #1d1d1d;
  }
  * { margin: 0; padding: 0; box-sizing: border-box; }
  html, body {
    width: 1200px;
    height: 1003px;
    overflow: hidden;
    background: var(--backdrop);
  }
  .canvas {
    position: relative;
    width: 1200px;
    height: 1003px;
  }
  .label {
    position: absolute;
    left: 252px;
    top: 127px;
    width: 696px;
    height: 748px;
    background: var(--label-stock);
    box-shadow: 0 2px 14px rgba(0,0,0,0.08);
  }
  .label svg { display: block; }
  .stripe-gold { stroke: var(--gold); stroke-width: 12; }
  .stripe-grey { stroke: var(--stripe-grey); stroke-width: 16; }
  .brand-name {
    font-family: "Josefin Sans", sans-serif;
    font-weight: 300;
    font-size: 72px;
    fill: var(--gold);
  }
  .brand-vertical {
    font-family: "Josefin Sans", sans-serif;
    font-weight: 400;
    font-size: 78px;
    fill: var(--slate);
  }
  .appellation {
    font-family: "Pinyon Script", cursive;
    font-size: 40px;
    fill: var(--gold);
  }
  .origin {
    font-family: "Josefin Sans", sans-serif;
    font-weight: 400;
    font-size: 15px;
    fill: var(--ink);
  }
  .legal {
    font-family: "Cormorant Garamond", serif;
    font-weight: 500;
    font-size: 10px;
    letter-spacing: 1.5px;
    fill: var(--ink);
  }
</style>
</head>
<body>
  <main class="canvas">
    <section class="label">
      <svg width="696" height="748" viewBox="0 0 696 748" xmlns="http://www.w3.org/2000/svg">
        <line class="stripe-gold" x1="552" y1="-2" x2="424" y2="130"/>
        <line class="stripe-grey" x1="289" y1="270" x2="0" y2="568"/>
        <text class="brand-name" x="356" y="226" text-anchor="middle" textLength="300" lengthAdjust="spacing">Clavine</text>
        <text class="brand-vertical" transform="translate(640,718) rotate(-90)" textLength="535" lengthAdjust="spacing">CLAVINE</text>
        <text class="appellation" x="345" y="590" text-anchor="middle">Burgundy Wine</text>
        <text class="origin" x="340" y="621" text-anchor="middle" textLength="260" lengthAdjust="spacing">PRODUCT OF FRANCE</text>
        <text class="legal" x="330" y="699" text-anchor="middle">ALC 15% BY VOL</text>
        <text class="legal" x="330" y="717" text-anchor="middle">750 ML</text>
      </svg>
    </section>
  </main>
</body>
</html>
```